DPM Marketing Postcard

Design a 2 Sided marketing postcard for our Real estate management caompany. Looking for a professional yet fresh look that will be printed on a 6"x9" glossy flier

Contact information is www.dunkeldmanagement-example.com dunkeldmanagement@dunkeldmail-example.com and 312-480-7193

WE are targeting small condo and town home properties to take on their administrative responsibilities of management

```html
<!DOCTYPE html>
<html lang="en">
<head>
<meta charset="utf-8">
<title>DPM Marketing Postcard</title>
<link href="https://fonts.googleapis.com/css2?family=Oswald:wght@700&family=Lato:wght@400;700&display=swap" rel="stylesheet">
<style>
  :root{
    --maroon:#5a0a0c;
    --grey:#8e8a8b;
    --grey-dark:#5c5859;
    --white:#ffffff;
    --bg:#e4e4e4;
    --ink:#3a3a3a;
    --photo-a:#c9a27c;
    --photo-b:#8a6a50;
  }
  *{box-sizing:border-box;margin:0;padding:0}
  html,body{width:1200px;height:1200px;overflow:hidden;background:var(--bg);font-family:"Lato",sans-serif}
  .canvas{position:relative;width:1200px;height:1200px}
  .postcard{position:absolute;left:210px;width:780px;height:520px;background:var(--white);overflow:hidden;box-shadow:0 6px 18px rgba(0,0,0,.15)}
  .postcard--front{top:50px}
  .postcard--back{top:630px}
  .postcard svg.shapes{position:absolute;inset:0}
  .photo-area{position:absolute;inset:0}
  .title{position:absolute;left:300px;right:40px;top:30px;text-align:center;font-family:"Oswald",sans-serif;font-weight:700;color:var(--grey-dark);font-size:26px;line-height:1.05;letter-spacing:.3px}
  .title span{display:block;color:var(--maroon);font-size:20px}
  .band-title{position:absolute;color:var(--white);font-weight:700;font-size:26px;letter-spacing:.5px}
  .bullets{position:absolute;color:var(--ink);font-size:12px;line-height:1.35;list-style:none}
  .bullets li{position:relative;padding-left:14px}
  .bullets li::before{content:"";position:absolute;left:2px;top:6px;width:5px;height:5px;border-radius:50%;background:currentColor}
  .contact{position:absolute;color:var(--white)}
  .contact__label{font-size:17px;font-weight:700;white-space:nowrap}
  .contact__item{display:flex;align-items:center;gap:6px;font-size:14px;font-weight:700;white-space:nowrap}
  .contact__item svg{width:13px;height:13px;fill:var(--white);flex:none}
  .back-block{position:absolute;left:28px;top:18px;width:480px;color:var(--white)}
  .back-block h3{font-size:20px;font-weight:700;margin-bottom:4px}
  .back-block .bullets{position:static;color:var(--white);font-size:11px;line-height:1.3}
  .back-list{left:30px;top:272px;width:440px;font-size:11.5px;line-height:1.35}
  .stamp-box{position:absolute;left:650px;top:40px;width:90px;height:90px;border:1.5px solid #333}
  .address-line{position:absolute;left:520px;width:230px;border-top:1.5px solid #555}
</style>
</head>
<body>
<div class="canvas">

  <!-- Front side -->
  <section class="postcard postcard--front">
    <svg class="shapes" viewBox="0 0 780 520" width="780" height="520">
      <rect x="0" y="100" width="780" height="44" fill="var(--maroon)"/>
      <rect x="0" y="262" width="780" height="44" fill="var(--maroon)"/>
      <rect x="0" y="430" width="780" height="90" fill="var(--grey)"/>
      <polygon points="262,0 276,0 448,520 434,520" fill="var(--grey)"/>
      <polygon points="234,0 262,0 434,520 406,520" fill="var(--maroon)"/>
    </svg>
    <svg class="photo-area" viewBox="0 0 780 520" width="780" height="520" role="img" aria-label="Photo of an open hand holding a key with a small wooden house keyring over a workbench">
      <defs>
        <linearGradient id="photoTone" x1="0" y1="0" x2="1" y2="1">
          <stop offset="0" stop-color="#d9d2cb"/>
          <stop offset=".5" stop-color="var(--photo-a)"/>
          <stop offset="1" stop-color="var(--photo-b)"/>
        </linearGradient>
      </defs>
      <polygon points="0,0 234,0 406,520 0,520" fill="url(#photoTone)"/>
    </svg>

    <h1 class="title">DUNKELD PROPERTY MANAGEMENT<span>(“DPM”)</span></h1>

    <h2 class="band-title" style="left:420px;top:105px">Who We Are?</h2>
    <ul class="bullets" style="left:390px;top:156px;width:370px">
      <li>A professional services organization with a focus on small (3-10 unit) residential buildings</li>
      <li>Over 30 years of combined experience in real estate and property management</li>
      <li>Professional, courteous, timely service that is technologically driven</li>
    </ul>

    <h2 class="band-title" style="left:430px;top:267px">Why use DPM?</h2>
    <ul class="bullets" style="left:440px;top:316px;width:325px">
      <li>Owners are rarely suited to manage associations and the burden often falls unfairly on one or two individuals to do all the work</li>
      <li>Low monthly fees tailored to your needs</li>
      <li>The association’s board of directors maintains control of all decision making</li>
    </ul>

    <div class="contact" style="left:460px;top:438px">
      <div class="contact__label">Contact Details</div>
      <div class="contact__item" style="margin-top:4px">
        <svg viewBox="0 0 24 24"><path d="M6.6 10.8a15 15 0 0 0 6.6 6.6l2.2-2.2a1 1 0 0 1 1-.25 11.4 11.4 0 0 0 3.6.57 1 1 0 0 1 1 1V20a1 1 0 0 1-1 1A17 17 0 0 1 3 4a1 1 0 0 1 1-1h3.5a1 1 0 0 1 1 1c0 1.25.2 2.45.57 3.57a1 1 0 0 1-.25 1z"/></svg>312-480-7193
      </div>
      <div class="contact__item" style="margin-top:4px">
        <svg viewBox="0 0 24 24"><circle cx="12" cy="12" r="10" fill="none" stroke="#fff" stroke-width="2"/><path d="M2 12h20M12 2c3 3 3 17 0 20M12 2c-3 3-3 17 0 20" fill="none" stroke="#fff" stroke-width="1.6"/></svg>www.dunkeldmanagement-example.com
      </div>
    </div>
  </section>

  <!-- Back side -->
  <section class="postcard postcard--back">
    <svg class="shapes" viewBox="0 0 780 520" width="780" height="520">
      <polygon points="0,0 515,0 580,252 0,252" fill="var(--maroon)"/>
      <polygon points="0,462 470,462 500,520 0,520" fill="var(--grey)"/>
    </svg>

    <div class="back-block">
      <h3>What we do</h3>
      <ul class="bullets">
        <li>Remove the administrative burden of managing small residential building estate and property management</li>
        <li>Utilize economies of scale to reduce expenses for all owners across a wide variety of service providers</li>
        <li>Technologically driven: collect all assessments and pay all bills</li>
        <li>Provide monthly accounting reconciliation and reporting</li>
        <li>Provide access to DPM’s client portal with a central repository of all association materials (bylaws, financials, meeting minutes, communications, etc.)</li>
        <li>Issue 1099s to all contractors as required by law</li>
        <li>Prepare year-end financial statements</li>
        <li>Lender and legal HOA documents for mortgage companies and sales</li>
      </ul>
    </div>

    <ul class="bullets back-list">
      <li>Cost effective property management solution for 3-10 unit buildings</li>
      <li>Prices starting as low as $100/month</li>
      <li>Utilize our economies of scale to reduce costs across existing services (trash, insurance, maintenance, etc.)</li>
      <li>Eliminate the unfair burden placed on a few owners to do all the work while others free ride</li>
      <li>Improve communication amongst all owners and board members</li>
      <li>The association’s board of directors maintain all decision-making power</li>
      <li>Utilize our vetted service providers for prompt job completion and fair pricing</li>
    </ul>

    <div class="contact" style="left:30px;top:482px">
      <div class="contact__label">Contact Details</div>
    </div>
    <div class="contact" style="left:190px;top:468px">
      <div class="contact__item">
        <svg viewBox="0 0 24 24"><path d="M6.6 10.8a15 15 0 0 0 6.6 6.6l2.2-2.2a1 1 0 0 1 1-.25 11.4 11.4 0 0 0 3.6.57 1 1 0 0 1 1 1V20a1 1 0 0 1-1 1A17 17 0 0 1 3 4a1 1 0 0 1 1-1h3.5a1 1 0 0 1 1 1c0 1.25.2 2.45.57 3.57a1 1 0 0 1-.25 1z"/></svg>312-480-7193
      </div>
      <div class="contact__item" style="margin-top:4px">
        <svg viewBox="0 0 24 24"><circle cx="12" cy="12" r="10" fill="none" stroke="#fff" stroke-width="2"/><path d="M2 12h20M12 2c3 3 3 17 0 20M12 2c-3 3-3 17 0 20" fill="none" stroke="#fff" stroke-width="1.6"/></svg>www.dunkeldmanagement-example.com
      </div>
    </div>

    <div class="stamp-box"></div>
    <div class="address-line" style="top:290px"></div>
    <div class="address-line" style="top:340px"></div>
    <div class="address-line" style="top:390px"></div>
  </section>

</div>
</body>
</html>
```